Hallowmere Business Card

This is the personal business card for Dr Glen Hallowmere and convers three area of his professional activity - all of them involve (foreign) languages:
o RQVB International Ltd - A translation company with 50 staff. Trades internationally
o TideLatch Ltd - a global online auction marketplace for translation services (startup)
o Vowelcraft - cutting edge technology from the brain sciences which helps learners assimilate the sound patterns of a new language (startup)

Target Market(s)

The card needs to have a "cutting edge" feel - but for a fairly conservative audience - academics, investors.

Industry/Entity Type

Business

Requirements
Must have
• Text:
Dr Glen Hallowmere

Co-founder RQVB International Ltd (Language translation)
Founder TideLatch Ltd (Translation marketplace)
Founder Vowelcraft (Language acquisition)

email: glen.morrow@lintmail.example
Phone: +64 21 555 3916
Twitter: @GlenMorrow4

```html
<!DOCTYPE html>
<html lang="en">
<head>
<meta charset="utf-8">
<title>Hallowmere Business Card</title>
<link href="https://fonts.googleapis.com/css2?family=Sorts+Mill+Goudy:ital@0;1&display=swap" rel="stylesheet">
<style>
  :root {
    --teal: #2f6b64;
    --stripe: #8c9a98;
    --ink: #1f1f1f;
    --paper: #ffffff;
  }
  html, body {
    margin: 0;
    padding: 0;
    width: 1200px;
    height: 686px;
    overflow: hidden;
    background: var(--paper);
  }
  .card {
    position: relative;
    width: 1200px;
    height: 686px;
    background: var(--paper);
    font-family: "Sorts Mill Goudy", Georgia, serif;
    color: var(--ink);
    overflow: hidden;
  }
  .stripe-band {
    position: absolute;
    left: 0; top: 0;
    width: 1200px; height: 120px;
    background: repeating-linear-gradient(90deg, var(--stripe) 0 24px, var(--paper) 24px 46px);
    -webkit-mask-image: linear-gradient(180deg, #000 0%, rgba(0,0,0,0.55) 45%, transparent 100%);
    mask-image: linear-gradient(180deg, #000 0%, rgba(0,0,0,0.55) 45%, transparent 100%);
  }
  .frame {
    position: absolute;
    left: 0; top: 0;
    width: 1200px; height: 686px;
  }
  .name-plate {
    position: absolute;
    left: 155px; top: 91px;
    width: 890px; height: 119px;
    box-sizing: border-box;
    background: var(--paper);
    border: 7px solid var(--teal);
    display: flex;
    align-items: center;
    justify-content: center;
  }
  .name-plate::before {
    content: "";
    position: absolute;
    inset: 5px;
    border: 2px solid var(--teal);
  }
  .name-plate__title {
    margin: 0;
    font-weight: 400;
    font-size: 46px;
    font-variant: small-caps;
    letter-spacing: 2px;
    color: var(--teal);
  }
  .roles {
    position: absolute;
    left: 90px; top: 285px;
    width: 460px;
    text-align: center;
    font-size: 17px;
    line-height: 30px;
  }
  .roles p { margin: 0 0 24px; }
  .contact {
    position: absolute;
    left: 70px; top: 470px;
    width: 500px;
    text-align: center;
    font-size: 31px;
    line-height: 42px;
  }
  .contact p { margin: 0; }
  .signature {
    position: absolute;
    left: 640px; top: 400px;
    width: 480px;
    text-align: center;
  }
  .signature__name {
    margin: 0;
    font-size: 30px;
    font-variant: small-caps;
    letter-spacing: 1px;
  }
  .signature__tagline {
    margin: 6px 0 0;
    font-size: 25px;
    font-style: italic;
  }
</style>
</head>
<body>
  <div class="card">
    <div class="stripe-band"></div>

    <svg class="frame" viewBox="0 0 1200 686" xmlns="http://www.w3.org/2000/svg">
      <rect x="34" y="103" width="1132" height="549" fill="none" stroke="var(--teal)" stroke-width="2"/>
      <ellipse cx="600" cy="100" rx="74" ry="66" fill="var(--teal)"/>
      <ellipse cx="600" cy="66" rx="34" ry="18" fill="#6f9b94" role="img" aria-label="Small leaf ornament"/>
    </svg>

    <header class="name-plate">
      <h1 class="name-plate__title">Dr. Glen Hallowmere</h1>
    </header>

    <section class="roles">
      <p>Co-founder RQVB International Ltd (Language<br>Translation)</p>
      <p>Founder TideLatch Ltd (Translation Marketplace)</p>
      <p>Founder Vowelcraft (Language Acquisition)</p>
    </section>

    <section class="contact">
      <p>Phone: +64 21 555 3916</p>
      <p>Twitter: @GlenMorrow4</p>
      <p>E-mail: glen.morrow@lintmail.example</p>
    </section>

    <section class="signature">
      <p class="signature__name">Glen Hallowmere</p>
      <p class="signature__tagline">Profession in Foreign Languages</p>
    </section>
  </div>
</body>
</html>
```